Torvel Law, PC Letterhead Design -- LAW FIRM

I am looking for a very elegant letterhead design for my personal injury law practice.
The letter head must have 4 different variations of the same thing meaning one design that has just a header, and another with a header and footer.
Elegance is key, I do not want it to be too bold. Please stay away from colors that are not black, white or gray or silver.
Please include a gradient style letterhead for the header while implementing the design of the logo found in folder #3
I have attached for you the logos and emblems for my company below.
In folders 1-4 you will find my actual logo.
In folder 5-6 you will find a shorter version of my logo, this can be implemented maybe in the footer + header design of the letter head (do not include this shortened version in the header).
In folders 7-8 you will find an emblem for my company.
Information that needs to be found on the letterhead is as follows:
A clearly written version of my company name: Torvel Law, PC
Address: 4718 Pemberly Avenue Suite #512, Beverly Hills, CA, 90210
Email: dorian@torvellaw.example
Telephone number: 310-555-0174

```html
<!DOCTYPE html>
<html lang="en">
<head>
<meta charset="utf-8">
<title>Torvel Law, PC — Letterhead</title>
<link href="https://fonts.googleapis.com/css2?family=Quicksand:wght@500;600&display=swap" rel="stylesheet">
<style>
  :root {
    --backdrop: #3a3a3a;
    --paper: #ffffff;
    --ink: #2b2b2b;
    --ink-strong: #1a1a1a;
    --band-dark: #6e6e6e;
    --band-mid: #a9a7a8;
    --band-light: #f2f2f2;
    --sig-fill: #ececec;
  }
  * { margin: 0; padding: 0; box-sizing: border-box; }
  html, body {
    width: 1200px; height: 1200px; overflow: hidden;
    background: var(--backdrop);
  }
  .letterhead {
    position: absolute; left: 176px; top: 0;
    width: 848px; height: 1200px;
    background: var(--paper);
    font-family: "Quicksand", sans-serif;
    font-weight: 500;
    color: var(--ink);
    overflow: hidden;
  }
  .brand {
    position: absolute; left: 80px; top: 102px;
    font-size: 27px; font-weight: 600; color: var(--ink-strong);
    letter-spacing: 0.5px; white-space: nowrap;
  }
  .address {
    position: absolute; left: 359px; top: 104px;
    font-size: 12.5px; line-height: 17.6px; white-space: nowrap;
    font-style: normal;
  }
  .contact {
    position: absolute; left: 611px; top: 104px;
    font-size: 12.8px; line-height: 17.6px; list-style: none;
  }
  .contact li { display: flex; align-items: center; gap: 6px; white-space: nowrap; }
  .contact svg { width: 10px; height: 10px; flex: none; }
  .recipient {
    position: absolute; left: 80px; top: 298px;
    font-size: 15.5px; line-height: 22.8px;
  }
  .salutation {
    position: absolute; left: 80px; top: 458px;
    font-size: 15.5px;
  }
  .body-copy {
    position: absolute; left: 80px; top: 502px; width: 705px;
    font-size: 15.4px; line-height: 22.8px; text-align: justify;
    letter-spacing: 0.18px;
  }
  .signature {
    position: absolute; left: 74px; top: 933px;
    width: 319px; height: 76px;
    background: var(--sig-fill); border-radius: 4px;
  }
  .footer-band {
    position: absolute; left: 0; bottom: 0; width: 848px; height: 84px;
    background: linear-gradient(90deg, var(--band-dark) 0%, var(--band-mid) 55%, var(--band-light) 100%);
  }
</style>
</head>
<body>
  <main class="letterhead">
    <header>
      <div class="brand">Torvel Law, PC</div>
      <address class="address">
        4718 Pemberly Avenue<br>
        Suite #512 Beverly Hills, CA, 90210
      </address>
      <ul class="contact">
        <li>
          <svg viewBox="0 0 10 10" aria-hidden="true"><rect x="0.8" y="1.8" width="8.4" height="6.4" fill="none" stroke="#2b2b2b" stroke-width="1.2"/><path d="M1 2.2 L5 5.4 L9 2.2" fill="none" stroke="#2b2b2b" stroke-width="1.1"/></svg>
          dorian@torvellaw.example
        </li>
        <li>
          <svg viewBox="0 0 10 10" aria-hidden="true"><path d="M2.2 1 L3.8 1 L4.4 3.2 L3.3 4 Q4.2 5.9 6 6.8 L6.8 5.7 L9 6.3 L9 7.9 Q8.6 9 7.4 9 Q1 8.3 1 2.4 Q1.1 1.1 2.2 1 Z" fill="#2b2b2b"/></svg>
          310-555-0174
        </li>
      </ul>
    </header>

    <section class="recipient">
      Mr. John Doe<br>
      President<br>
      Strategy Accountants<br>
      111 Street Name,<br>
      City State, 12345
    </section>

    <p class="salutation">Dear</p>

    <section class="body-copy">
      Lorem ipsum dolor sit amet, consectetur adipiscing elit. Aenean ut ipsum eget massa hendrerit vestibulum vel in velit. Donec pretium neque velit.<br>
      Aliquam porta lectus nec mauris ornare venenatis. Vivamus non est turpis, et cursus sem. Mauris vehicula erat in diam auctor at bibendum nisl lacinia.<br>
      Morbi imperdiet neque vehicula nunc convallis gravida. Vestibulum iaculis pretium placerat. Integer consequat, est sit amet facilisis eleifend, nibh nibh varius orci, eget dapibus arcu dui non purus. Pellentesque in magna mauris. Duis enim sapien, dictum vitae condimentum a, pulvinar vel lacus. Mauris et molestie nibh. Vestibulum vitae nulla at metus elementum porta sit amet interdum elit. Nulla sollicitudin neque eu nulla volutpat congue.<br>
      Etiam pellentesque, velit id dapibus fermentum, turpis sapien ornare dui, ac tincidunt ligula odio congue purus. Nunc sed ante dui, in porta lectus. Cras nec sem lorem. In hac habitasse platea dictumst. Maecenas id diam quis dui porta tristique. Sed id egestas felis. Donec ullamcorper mattis posuere. Phasellus fermentum eleifend tortor vel dapibus. Vestibulum ante ipsum.
    </section>

    <div class="signature" role="img" aria-label="Handwritten signature of the sender"></div>

    <div class="footer-band" role="img" aria-label="Decorative grey footer band fading from dark to light"></div>
  </main>
</body>
</html>
```